Postcard Design

Looking for 4.25 x6 postcard design for mass mailing
Design should be eye catching, energetic and draw the viewer in

Data for postcard to include:
Logo and slogan
Pediatric Occupational, Physical and Speech Therapy Services; Assistive Technology Evaluation and Training

Speech-Language Therapy
oral motor skills
speech delays
language skills
Articulation
Voice
fluency
cognitive skills
feeding disorders
Play skills

OCCUPATIONAL THERAPY
Our occupational therapists use play in therapy to help your child develop the skills he/she needs to perform their job of living and playing, including but not limited to:
- Increasing independence in self-care skills such as feeding, dressing and grooming
- Improving developmental skills such as rolling, sitting, standing
- Improving their sensory processing, balance, coordination and motor planning
- Difficulty tolerating clothing
- Poor balance - doesn't ride a bike/climb on slides, falls frequently, cries when moved unexpectedly
- Intolerance to textures/odors/loud sounds/movement
- Delayed handwriting and fine motor skills and/or
avoids fine motor activities such as using crayons, fasteners on clothing, pencils
- Limited diet-refuses to try new foods, gags when trying new tastes, textures
- Appears extremely anxious, states frequent fears of harmless things

CONTACT US TODAY for a FREE 15 minute consultation/Screen
(301) 555-4182
info@brightwillowkids.example
www.brightwillowkids.example

Physical therapy
Delayed crawling / walking
Persistent toe walking habits
Poor unsupported sitting/standing balance
Trouble learning how to jump, skip, ride a bike
Decreased ability to throw and catch a ball
Delayed motor milestones
Need for wheelchair mobility training
Balance coordination and motor planning difficulty
Strength , muscle tone and/ R range of motion impairment
Sports injuries
Postural control and positioning difficulty

```html
<!DOCTYPE html>
<html lang="en">
<head>
<meta charset="utf-8">
<title>Bright Willow Kids – Postcard</title>
<link href="https://fonts.googleapis.com/css2?family=Fjalla+One&family=Open+Sans:ital,wght@0,400;0,600;0,700;1,400&display=swap" rel="stylesheet">
<style>
:root{
  --blue:#2a7bc4;
  --blue-deep:#1f6db5;
  --teal:#1fa69a;
  --teal-dark:#17968b;
  --orange:#e8a25c;
  --orange-light:#f1c26a;
  --yellow:#f5d24a;
  --white:#ffffff;
  --ink:#2166b0;
  --bg:#ecebe8;
}
*{box-sizing:border-box;margin:0;padding:0}
html,body{width:1200px;height:1200px;overflow:hidden;background:var(--bg)}
body{font-family:"Open Sans",sans-serif;position:relative}
.card{position:absolute;left:190px;width:820px;height:580px;background:var(--white);overflow:hidden;box-shadow:0 2px 8px rgba(0,0,0,.15)}
.card--front{top:10px}
.card--back{top:610px}

/* front */
.brand{position:absolute;left:50px;top:54px;display:flex;align-items:center;gap:12px}
.brand__mark{width:34px;height:34px;border-radius:50%;background:var(--teal)}
.brand__name{font-weight:600;font-size:25px;color:var(--ink)}
.brand__slogan{position:absolute;left:96px;top:94px;font-style:italic;font-size:12px;color:var(--ink)}
.services-band{position:absolute;left:0;top:140px;width:420px;height:156px;background:linear-gradient(90deg,var(--orange),var(--orange-light));padding:20px 0 0 38px}
.services-band p{font-family:"Fjalla One",sans-serif;color:var(--white);font-size:21.5px;line-height:32px}
.offer-band{position:absolute;left:0;top:296px;width:420px;height:146px;background:var(--teal);padding:24px 0 0 38px;color:var(--white);font-weight:600}
.offer-band .lead{font-size:19px;letter-spacing:.5px}
.offer-band .big{font-weight:700;font-size:34px;line-height:40px;letter-spacing:.5px}
.offer-band .tail{font-size:19px;letter-spacing:.5px}
.contacts{position:absolute;left:42px;top:464px;list-style:none}
.contacts li{display:flex;align-items:center;gap:16px;font-weight:600;font-size:15.5px;color:var(--ink);height:26px}
.contacts svg{width:16px;height:16px}
.front-art{position:absolute;inset:0;width:820px;height:580px;pointer-events:none}

/* back */
.speech{position:absolute;left:0;top:0;width:580px;height:86px;background:var(--teal);clip-path:polygon(0 0,100% 0,93% 100%,0 100%);padding:10px 0 0 26px;color:var(--white)}
.section-title{font-family:"Fjalla One",sans-serif;font-size:15px;letter-spacing:.3px}
.speech ul{list-style:none;display:grid;grid-template-columns:118px 118px 92px 118px 60px;gap:3px 0;margin-top:6px;font-size:11px}
.speech li::before,.ot li::before,.pt li::before{content:"▪";margin-right:6px;font-size:8px}
.ot{position:absolute;left:0;top:86px;width:560px;height:282px;background:var(--blue);padding:12px 0 0 28px;color:var(--white)}
.ot .intro{width:345px;font-size:11px;line-height:14px}
.ot .section-title{color:var(--yellow);font-size:15px;margin-right:4px}
.ot ul{list-style:none;margin-top:8px;width:355px;font-size:10px;line-height:12.5px}
.ot li{margin-bottom:3px;padding-left:12px;text-indent:-12px}
.pt{position:absolute;left:0;top:368px;width:540px;height:212px;background:linear-gradient(90deg,var(--orange-light),var(--orange));padding:14px 0 0 28px;color:var(--white)}
.pt .section-title{font-size:18px;line-height:26px}
.pt .cols{display:flex;gap:24px}
.pt ul{list-style:none;font-size:10px;line-height:12px}
.pt .col-a{width:165px}
.pt .col-a ul{margin-top:4px}
.pt .col-b{width:180px;margin-top:2px}
.pt li{margin-bottom:6px;padding-left:12px;text-indent:-12px}
.pt .wide{width:360px}
.back-art{position:absolute;inset:0;width:820px;height:580px}
</style>
</head>
<body>

<section class="card card--front">
  <svg class="front-art" viewBox="0 0 820 580">
    <defs>
      <linearGradient id="meadow" x1="0" y1="0" x2="0" y2="1">
        <stop offset="0" stop-color="#9fb3a4"/>
        <stop offset=".45" stop-color="#7fa46a"/>
        <stop offset="1" stop-color="#4f9a32"/>
      </linearGradient>
    </defs>
    <path d="M500 0 C 380 120 340 300 390 440 L 440 580 L 820 580 L 820 0 Z" fill="var(--white)"/>
    <path d="M505 0 L560 0 C 440 110 400 260 430 420 C 440 480 470 540 520 580 L 490 580 C 420 500 390 400 395 300 C 400 180 440 80 505 0 Z" fill="var(--blue)"/>
    <path d="M560 0 L820 0 L820 580 L520 580 C 440 500 420 380 430 300 C 440 180 480 80 560 0 Z" fill="url(#meadow)" role="img" aria-label="Photo of three children jumping for a ball on a grassy meadow"/>
    <path d="M440 580 C 470 520 510 500 530 470 C 500 440 460 450 420 480 C 380 510 360 560 330 580 Z" fill="var(--teal)" opacity=".95"/>
  </svg>

  <div class="brand">
    <span class="brand__mark"></span>
    <span class="brand__name">Bright Willow Kids</span>
  </div>
  <p class="brand__slogan">Improving skills and function for daily Living</p>

  <div class="services-band">
    <p>Pediatric Occupational,<br>Physical and Speech Therapy<br>Services; Assistive Technology<br>Evaluation and Training</p>
  </div>

  <div class="offer-band">
    <p class="lead">CONTACT US TODAY FOR A</p>
    <p class="big">FREE 15 MINUTE</p>
    <p class="tail">CONSULTATION/SCREEN</p>
  </div>

  <ul class="contacts">
    <li><svg viewBox="0 0 16 16"><path d="M4 1 L6.5 1 L7.5 5 L5.5 6.3 C6.3 8.3 7.7 9.8 9.7 10.6 L11 8.5 L15 9.5 L15 12 C15 13.5 13.6 15 12 15 C6.5 14.5 1.5 9.5 1 4 C1 2.4 2.5 1 4 1 Z" fill="var(--ink)"/></svg>(301) 555-4182</li>
    <li><svg viewBox="0 0 16 16"><rect x="1" y="3" width="14" height="10" fill="var(--ink)"/><path d="M1 3 L8 9 L15 3" stroke="#fff" stroke-width="1.3" fill="none"/></svg>info@brightwillowkids.example</li>
    <li><svg viewBox="0 0 16 16"><circle cx="8" cy="8" r="7" fill="var(--ink)"/><path d="M1 8 H15 M8 1 V15 M8 1 C4 5 4 11 8 15 M8 1 C12 5 12 11 8 15" stroke="#fff" stroke-width="1" fill="none"/></svg>www.brightwillowkids.example</li>
  </ul>
</section>

<section class="card card--back">
  <svg class="back-art" viewBox="0 0 820 580">
    <path d="M560 86 C 600 150 610 260 590 370 C 570 470 520 540 480 580 L 540 580 C 580 520 620 450 630 360 C 640 250 620 150 580 86 Z" fill="var(--teal)"/>
  </svg>

  <div class="speech">
    <h2 class="section-title">SPEECH-LANGUAGE THERAPY</h2>
    <ul>
      <li>Oral Motor Skills</li><li>Speech Delays</li><li>Play Skills</li><li>Cognitive skills</li><li>Voice</li>
      <li>Articulation</li><li>Language Skills</li><li>Fluency</li><li>Feeding Disorders</li>
    </ul>
  </div>

  <div class="ot">
    <p class="intro"><span class="section-title">OCCUPATIONAL THERAPY</span> Our occupational therapists use play in therapy to help your child develop the skills he/she needs to perform their job of living and playing, including but not limited to:</p>
    <ul>
      <li>Increasing independence in self-care skills such as feeding, dressing and grooming</li>
      <li>Improving developmental skills such as rolling, sitting, standing</li>
      <li>Improving their sensory processing, balance, coordination and motor planning</li>
      <li>Difficulty tolerating clothing &nbsp;&nbsp;▪ Fasteners on clothing, pencils</li>
      <li>Poor balance - doesn't ride a bike/climb on slides, falls frequently, cries when moved unexpectedly</li>
      <li>Intolerance to textures/odors/loud sounds/movement</li>
      <li>Delayed handwriting and fine motor skills and/or avoids fine motor activities such as using crayons</li>
      <li>Limited diet-refuses to try new foods, gags when trying new tastes, textures</li>
      <li>Appears extremely anxious, states frequent fears of harmless things</li>
    </ul>
  </div>

  <div class="pt">
    <div class="cols">
      <div class="col-a">
        <h2 class="section-title">PHYSICAL THERAPY</h2>
        <ul>
          <li>Delayed crawling / walking</li>
          <li>Poor unsupported sitting/ standing balance</li>
          <li>Delayed motor milestones</li>
          <li>Sports injuries</li>
          <li>Persistent toe walking habits</li>
        </ul>
      </div>
      <ul class="col-b">
        <li>Need for wheelchair mobility training</li>
        <li>Trouble learning how to jump, skip, ride a bike</li>
        <li>Balance coordination and motor planning difficulty</li>
        <li>Strength , muscle tone and/ R range of motion impairment</li>
      </ul>
    </div>
    <ul class="wide">
      <li>Postural control and positioning difficulty</li>
    </ul>
  </div>

  <svg class="back-art" viewBox="0 0 820 580">
    <defs>
      <linearGradient id="room" x1="0" y1="0" x2="1" y2="1">
        <stop offset="0" stop-color="#e7e3df"/><stop offset="1" stop-color="#c98a7c"/>
      </linearGradient>
      <linearGradient id="clinic" x1="0" y1="0" x2="0" y2="1">
        <stop offset="0" stop-color="#eef1f4"/><stop offset="1" stop-color="#9fb6cf"/>
      </linearGradient>
    </defs>
    <circle cx="558" cy="160" r="52" fill="url(#room)" stroke="var(--orange-light)" stroke-width="5" role="img" aria-label="Photo of a therapist working with a young girl at a desk"/>
    <circle cx="600" cy="285" r="70" fill="url(#room)" stroke="var(--orange-light)" stroke-width="6" role="img" aria-label="Photo of a therapist doing a play activity with a child"/>
    <circle cx="562" cy="420" r="56" fill="url(#clinic)" stroke="var(--orange-light)" stroke-width="5" role="img" aria-label="Photo of a child balancing on an exercise ball with a therapist"/>
  </svg>
</section>

</body>
</html>
```